Soy Candle Business needs a label design

We need a label design for a new company selling soy candles - Velvet Hearth Co.

We are using apothecary jars in 3 sizes.
As per attached candles will be dressed with a beautiful black bow and all finished with a diamante in centre of bow.

We would like label done on lid of candle jars - 5cm circle (5cm from one side to the other), this way one label will fit each product size. Label will be done as a sticker.

We are thinking of the background colour to be black, however are open to recommendations. We want label to be classy, elegant and simple.

Inspiration for candle design came from attached invitation that features the bow, and beautiful vintage paper on top area.

Label should include the following 3 pieces of information:
Velvet Hearth Co (company name)
Coconut Lime (this will change depending on fragrance)
Soy Candle

Velvet Hearth Co does not have a company logo... what is done for the label will set tone for what is done across other elements of business moving forward.

Industry/Entity Type

Business

Requirements
Must have
• Velvet Hearth Co
Fragrance Flavour
Soy Candle

```html
<!DOCTYPE html>
<html lang="en">
<head>
<meta charset="utf-8">
<title>Velvet Hearth Co — Soy Candle Lid Labels</title>
<link href="https://fonts.googleapis.com/css2?family=Jost:wght@400&display=swap" rel="stylesheet">
<style>
  :root {
    --paper: #ffffff;
    --label: #000000;
    --ink-light: #ffffff;
    --ink-dark: #111111;
    --mango: #e57d2b;
    --caramel: #d6d2cc;
    --pear: #b53fc9;
    --lemongrass: #c9e34a;
    --lime: #5fe33a;
  }
  html, body {
    margin: 0;
    padding: 0;
    width: 1200px;
    height: 857px;
    overflow: hidden;
    background: var(--paper);
  }
  .sheet { display: block; width: 1200px; height: 857px; }
  .sheet text { font-family: "Jost", "Futura", sans-serif; font-weight: 400; }
  .label-disc { fill: var(--label); }
  .brand-name { fill: var(--ink-light); font-size: 48px; letter-spacing: 1px; }
  .product-type { fill: var(--ink-light); font-size: 26px; letter-spacing: 0.5px; }
  .ring-text { letter-spacing: 0.5px; }
  .ring-mango { fill: var(--mango); font-size: 10px; }
  .ring-caramel { fill: var(--caramel); font-size: 7.5px; }
  .ring-pear { fill: var(--pear); font-size: 10px; }
  .ring-lemongrass { fill: var(--lemongrass); font-size: 7.5px; }
  .ring-lime { fill: var(--lime); font-size: 26px; }
  .size-caption { fill: var(--ink-dark); font-size: 14px; letter-spacing: 1.5px; }
</style>
</head>
<body>
<svg class="sheet" viewBox="0 0 1200 857" xmlns="http://www.w3.org/2000/svg">
  <defs>
    <path id="ring-6cm-top" d="M43,188 a100,100 0 1 1 200,0 a100,100 0 1 1 -200,0"/>
    <path id="ring-6cm-bottom" d="M43,486 a100,100 0 1 1 200,0 a100,100 0 1 1 -200,0"/>
    <path id="ring-5cm-top" d="M349,198 a62,62 0 1 1 124,0 a62,62 0 1 1 -124,0"/>
    <path id="ring-5cm-bottom" d="M349,486 a62,62 0 1 1 124,0 a62,62 0 1 1 -124,0"/>
    <path id="ring-large" d="M661,290 a238,238 0 1 1 476,0 a238,238 0 1 1 -476,0"/>

    <g id="label-centre">
      <text class="brand-name" x="10" y="-30" text-anchor="middle">Velvet Hearth</text>
      <text class="brand-name" x="10" y="18" text-anchor="middle">Co</text>
      <text class="product-type" x="10" y="84" text-anchor="middle">soy candle</text>
    </g>
  </defs>

  <!-- 6cm label: mango papaya -->
  <g class="label label-6cm">
    <circle class="label-disc" cx="143" cy="188" r="110"/>
    <text class="ring-text ring-mango" textLength="620" lengthAdjust="spacing">
      <textPath href="#ring-6cm-top">mango papaya · mango papaya · mango papaya · mango papaya · mango papaya · mango papaya · mango papaya ·</textPath>
    </text>
    <use href="#label-centre" transform="translate(143,188) scale(0.42)"/>
  </g>

  <!-- 5cm label: creme caramel -->
  <g class="label label-5cm">
    <circle class="label-disc" cx="411" cy="198" r="70"/>
    <text class="ring-text ring-caramel" textLength="384" lengthAdjust="spacing">
      <textPath href="#ring-5cm-top">creme caramel · creme caramel · creme caramel · creme caramel · creme caramel · creme caramel ·</textPath>
    </text>
    <use href="#label-centre" transform="translate(411,198) scale(0.27)"/>
  </g>

  <!-- 6cm label: french pear -->
  <g class="label label-6cm">
    <circle class="label-disc" cx="143" cy="486" r="110"/>
    <text class="ring-text ring-pear" textLength="620" lengthAdjust="spacing">
      <textPath href="#ring-6cm-bottom">french pear · french pear · french pear · french pear · french pear · french pear · french pear · french pear ·</textPath>
    </text>
    <use href="#label-centre" transform="translate(143,486) scale(0.42)"/>
  </g>

  <!-- 5cm label: lemongrass & sage -->
  <g class="label label-5cm">
    <circle class="label-disc" cx="411" cy="486" r="70"/>
    <text class="ring-text ring-lemongrass" textLength="384" lengthAdjust="spacing">
      <textPath href="#ring-5cm-bottom">lemongrass &amp; sage · lemongrass &amp; sage · lemongrass &amp; sage · lemongrass &amp; sage · lemongrass &amp; sage ·</textPath>
    </text>
    <use href="#label-centre" transform="translate(411,486) scale(0.27)"/>
  </g>

  <text class="size-caption" x="148" y="614" text-anchor="middle">6cm version</text>
  <text class="size-caption" x="413" y="613" text-anchor="middle">5cm version</text>

  <!-- Enlarged label: coconut lime -->
  <g class="label label-large">
    <circle class="label-disc" cx="899" cy="290" r="262"/>
    <text class="ring-text ring-lime" textLength="1480" lengthAdjust="spacing">
      <textPath href="#ring-large">coconut lime · coconut lime · coconut lime · coconut lime · coconut lime · coconut lime · coconut lime · coconut lime ·</textPath>
    </text>
    <use href="#label-centre" transform="translate(899,290)"/>
  </g>

  <!-- Brand mark disc -->
  <g class="brand-mark">
    <circle class="label-disc" cx="886" cy="707" r="75"/>
    <g transform="translate(886,707) scale(0.3)">
      <text class="brand-name" x="10" y="-30" text-anchor="middle">Velvet Hearth</text>
      <text class="brand-name" x="10" y="18" text-anchor="middle">Co</text>
      <text class="product-type" x="10" y="84" text-anchor="middle">soy candles</text>
    </g>
  </g>
  <text class="size-caption" x="892" y="809" text-anchor="middle">imagery used as logo</text>
</svg>
</body>
</html>
```